International Manufacturing Business Needs A Heavy Hitting Wordpress Design!

We need wordpress template designs for a new website for our UK based International company Tolvane Engineering Ltd. We manufacture and supply steel security doors and window units. We would like designs that feature the black and yellow industrial "stripes" that can be seen at our current site www.tolvadoors.com. The final design should communicate strength, power and weight to represent the quality of the products and the security that they provide.

It feels like we need 3 different types of page to be able to be created as per the current website at www.tolvasecuredoors.com.

Homepage
Products/Accessories
Leadtimes/Downloads/Contact

It may be that 3 different page types can be created with one template. I'm totally open to this.

I don't like the way that the site currently handles product images, nobody wants to click on even thumbnail to see the product. http://tolvasecuredoors.com/products/personnel-doors/

Totally open to suggestions on layout to enable the feeling outlined in the brief above.

Please ask if anything is not clear or you need answers to drill down on specifics.

Sick

Target Market(s)

Businesses that buy steel doors

Font styles to use
Sans Serif
Other font styles liked:
• Copperplate Gothic Bold - For Company Name but we are open to suggestions

Colors

Designer to choose colors to be used in the design.

Requirements
Must have
• Professional looking, clean design
• Conveys strength, power and weight to represent the quality of the products, the characteristics of steel and the security that they provide.
• Incorporates black and yellow stripes of our branding
• Ability to create pages with content as seen at www.tolvasecuredoors.com
• A better way of showing the product images
Nice to have
• If possible. a design that gives off the feeling that not only do we supply the products we also make them in house too. I don't know what this looks like but a way of differentiating between a supply only business and one that manufacturers the product too.
Should not have
• We don't like the current thumbnail method of showing the product images

```html
<!DOCTYPE html>
<html lang="en">
<head>
<meta charset="utf-8">
<title>Tolvane Engineering Ltd – Steel Security Doors</title>
<link rel="stylesheet" href="https://fonts.googleapis.com/css2?family=Source+Sans+3:wght@400;600;700;800&family=Montserrat:wght@400;500;600;700&display=swap">
<style>
  :root{
    --yellow:#fbd341;
    --yellow-deep:#f6c82b;
    --ink:#141414;
    --charcoal:#232323;
    --hero-grey:#6f6f6f;
    --hero-band:#7d7a68;
    --white:#ffffff;
    --rule:#9a9a9a;
    --teal:#2aa7c9;
    --body:#2a2a2a;
  }
  *{box-sizing:border-box;margin:0;padding:0}
  html,body{width:1200px;height:1200px;overflow:hidden;background:var(--white)}
  body{position:relative;font-family:"Montserrat",sans-serif;color:var(--body)}
  .abs{position:absolute}

  /* header */
  .site-header{left:268px;top:0;width:665px;height:74px;background:var(--charcoal)}
  .brand{left:22px;top:20px;display:flex;align-items:center;gap:7px}
  .brand-mark{width:14px;height:30px;background:var(--yellow)}
  .brand-name{font-family:"Source Sans 3",sans-serif;font-weight:700;font-size:10.5px;line-height:12px;color:var(--white);text-transform:uppercase;letter-spacing:.3px;width:104px}
  .main-nav{left:160px;top:28px;display:flex;gap:12px;font-family:"Source Sans 3",sans-serif;font-weight:700;font-size:15px;color:var(--white);letter-spacing:-.2px;white-space:nowrap}
  .main-nav span::before{content:"v";color:var(--yellow);font-size:11px;font-weight:600;margin-right:4px}
  .cart{left:612px;top:16px;width:53px;height:50px;background:var(--yellow);display:flex;align-items:center;justify-content:center}
  .top-rule{left:0;top:74px;width:1200px;height:6px;background:var(--yellow)}

  /* hero */
  .hero{left:0;top:80px;width:1200px;height:346px;background:var(--hero-grey);overflow:hidden}
  .hero-stripes{left:0;top:0;width:1200px;height:84px}
  .contact-bar{left:596px;top:80px;width:337px;height:38px;background:var(--yellow);clip-path:polygon(12px 0,100% 0,100% 100%,0 100%);display:flex;align-items:center;font-family:"Source Sans 3",sans-serif;font-weight:600;font-size:17px;color:var(--ink)}
  .contact-bar .phone{display:flex;align-items:center;gap:5px;margin-left:16px}
  .contact-bar .quote{margin-left:52px;font-weight:700}
  .hero-photo-a{left:187px;top:110px;width:173px;height:244px;background:linear-gradient(160deg,#2a2a2a,#c8361f 45%,#a62514 60%,#1c1c1c);border:2px solid var(--white)}
  .hero-accent{left:360px;top:118px;width:8px;height:230px;background:var(--yellow)}
  .hero-photo-b{left:368px;top:130px;width:222px;height:201px;background:linear-gradient(100deg,#55604a,#98a68f 45%,#d9ddd6 70%,#7d8776);border:1px solid var(--yellow)}
  .hero-title{left:570px;top:178px;font-family:"Source Sans 3",sans-serif;font-weight:800;font-size:31px;line-height:36px;color:var(--white);text-transform:uppercase;letter-spacing:.3px}
  .hero-title em{font-style:normal;color:var(--yellow)}
  .arrow{top:224px}

  /* feature boxes */
  .feature{top:374px;height:158px;background:var(--ink);text-align:center;padding-top:28px}
  .feature--raised{top:374px;height:164px;background:var(--charcoal)}
  .feature h3{font-family:"Source Sans 3",sans-serif;font-weight:700;font-size:14px;color:var(--yellow);margin-top:6px;letter-spacing:.3px}
  .feature p{font-size:8.5px;line-height:14.5px;font-weight:600;color:var(--white);margin:10px auto 0;width:170px}
  .feature--raised p{font-family:"Source Sans 3",sans-serif;font-weight:400;font-size:10.5px;line-height:13px;width:160px;margin-top:8px}

  /* what we do */
  .intro{left:277px;top:554px;width:320px}
  .intro h2{font-family:"Source Sans 3",sans-serif;font-weight:800;font-size:24px;line-height:26px;color:var(--ink)}
  .intro h2 em{font-style:normal;color:var(--yellow-deep)}
  .intro h4{font-family:"Source Sans 3",sans-serif;font-weight:800;font-size:21px;line-height:30px;color:var(--ink)}
  .intro p{font-family:"Source Sans 3",sans-serif;font-size:10px;line-height:13px;letter-spacing:-.1px;color:var(--body);margin-top:3px}
  .btn{left:276px;top:700px;width:98px;height:23px;background:var(--ink);color:var(--white);font-size:7px;font-weight:700;display:flex;align-items:center;justify-content:center}
  .service{width:156px}
  .service .hex{position:absolute;left:0;top:0}
  .service h5{position:absolute;left:46px;top:13px;font-size:8.6px;font-weight:700;color:var(--ink);white-space:nowrap}
  .service p{position:absolute;left:0;top:52px;font-size:7.6px;line-height:15px;font-weight:600;letter-spacing:-.1px;color:var(--ink);width:160px}
  .col-rule{top:555px;width:150px;height:1px;background:var(--rule)}

  /* technology */
  .tech-photo{left:0;top:794px;width:396px;height:382px;background:linear-gradient(120deg,#6a5a4a,#b9b4ab 35%,#3aa7d6 48%,#9ea3a6 62%,#5b5f63)}
  .tech-panel{left:396px;top:794px;width:804px;height:382px;background:var(--yellow)}
  .tech-copy{left:600px;top:838px;width:324px;border-left:1px solid var(--white);padding-left:7px}
  .tech-copy small{display:block;font-size:5.5px;font-weight:700;color:var(--ink)}
  .tech-copy h2{font-family:"Montserrat",sans-serif;font-weight:700;font-size:16px;letter-spacing:3px;color:var(--ink);margin-top:4px}
  .tech-copy p{font-size:8px;line-height:15px;font-weight:600;color:var(--ink);margin-top:3px}
  .acc{left:600px;width:324px;background:var(--white);border:1px solid #f0e1a0}
  .acc-head{height:29px;display:flex;align-items:center;justify-content:space-between;padding:0 9px;font-size:7.3px;font-weight:600;color:var(--ink)}
  .acc-toggle{width:17px;height:17px;background:var(--ink);display:flex;align-items:center;justify-content:center}
  .acc-body{border-top:1px solid #eee;padding:10px 9px;font-size:7.8px;line-height:15px;font-weight:600;color:var(--ink);height:67px}
</style>
</head>
<body>

<header class="abs site-header">
  <div class="abs brand"><span class="brand-mark"></span><span class="brand-name">Tolvane Engineering Ltd.</span></div>
  <nav class="abs main-nav"><span>HOME</span><span>PRODUCTS/ACCESSORIES</span><span>DOWNLOADS</span><span>CONTACT</span></nav>
  <div class="abs cart">
    <svg width="22" height="18" viewBox="0 0 22 18"><path d="M1 2h3l2 9h10l2-7H5" fill="none" stroke="#141414" stroke-width="1.6"/><circle cx="8" cy="15" r="1.5" fill="#141414"/><circle cx="15" cy="15" r="1.5" fill="#141414"/><circle cx="19" cy="3" r="3" fill="#141414"/><text x="19" y="4.5" font-size="4.5" fill="#fbd341" text-anchor="middle" font-family="Montserrat,sans-serif">0</text></svg>
  </div>
</header>
<div class="abs top-rule"></div>

<section class="abs hero">
  <svg class="abs hero-stripes" viewBox="0 0 1200 84" preserveAspectRatio="none">
    <rect width="1200" height="84" fill="#7d7a68"/>
    <g fill="#6b6b6b">
      <polygon points="0,0 150,0 80,84 0,84"/>
      <polygon points="260,0 400,0 330,84 190,84"/>
      <polygon points="500,0 640,0 570,84 430,84"/>
      <polygon points="760,0 900,0 830,84 690,84"/>
      <polygon points="1020,0 1160,0 1090,84 950,84"/>
    </g>
  </svg>
  <svg class="abs arrow" style="left:22px" width="26" height="42" viewBox="0 0 26 42"><path d="M22 4 6 21l16 17" fill="none" stroke="#fff" stroke-width="6"/></svg>
  <svg class="abs arrow" style="left:1114px" width="26" height="42" viewBox="0 0 26 42"><path d="M4 4l16 17L4 38" fill="none" stroke="#fff" stroke-width="6"/></svg>
</section>

<div class="abs contact-bar">
  <span class="phone"><svg width="20" height="20" viewBox="0 0 24 24"><path d="M6.6 10.8a15 15 0 0 0 6.6 6.6l2.2-2.2c.3-.3.7-.4 1-.2 1.1.4 2.3.6 3.6.6.6 0 1 .4 1 1V20c0 .6-.4 1-1 1A17 17 0 0 1 3 4c0-.6.4-1 1-1h3.5c.6 0 1 .4 1 1 0 1.3.2 2.5.6 3.6.1.3 0 .7-.2 1z" fill="#141414"/></svg>+44 (0)1632 960 418</span>
  <span class="quote">Get a quote</span>
</div>

<div class="abs hero-accent"></div>
<div class="abs hero-photo-a" role="img" aria-label="Red steel security door with numbered locking point details"></div>
<div class="abs hero-photo-b" role="img" aria-label="Worker in protective suit spray painting a steel door in the finishing booth"></div>
<h1 class="abs hero-title">We combine a high level<br>of security <em>with</em><br><em>exceptional value</em></h1>

<div class="abs feature" style="left:268px;width:222px">
  <svg width="36" height="30" viewBox="0 0 36 30"><rect x="10" y="0" width="10" height="6" fill="#fbd341"/><rect x="8" y="8" width="20" height="5" fill="#fff"/><rect x="2" y="15" width="32" height="7" fill="#2aa7c9"/><rect x="4" y="24" width="4" height="6" fill="#2aa7c9"/><rect x="28" y="24" width="4" height="6" fill="#2aa7c9"/></svg>
  <h3>INDUSTRIAL PROCESS</h3>
  <p>Curabitur vel fermentum augue, quis vulputate diam</p>
</div>
<div class="abs feature feature--raised" style="left:490px;width:221px;padding-top:20px">
  <svg width="58" height="42" viewBox="0 0 58 42"><circle cx="42" cy="14" r="13" fill="none" stroke="#fff" stroke-width="2"/><path d="M42 7v7l5 3" stroke="#fff" stroke-width="2" fill="none"/><path d="M2 34V20l8-7h26v21z" fill="#fff"/><circle cx="12" cy="35" r="4" fill="#fff" stroke="#232323" stroke-width="2"/><circle cx="32" cy="35" r="4" fill="#fff" stroke="#232323" stroke-width="2"/><text x="22" y="29" font-size="10" font-weight="700" font-family="Montserrat,sans-serif" fill="#232323">24</text></svg>
  <h3>DELIVERY</h3>
  <p>We use a select range of haulage companies to deliver our products, they have a proven record of delivering safely and on time.</p>
</div>
<div class="abs feature" style="left:711px;width:222px">
  <svg width="34" height="32" viewBox="0 0 34 32"><rect x="24" y="0" width="4" height="14" fill="#fff"/><rect x="18" y="4" width="4" height="10" fill="#fbd341"/><path d="M2 32V18l8-4v4l8-4v4l8-4v18z" fill="#e0743a"/><rect x="5" y="22" width="6" height="3" fill="#fff"/><rect x="15" y="22" width="6" height="3" fill="#fff"/></svg>
  <h3>INDUSTRIAL PROCESS</h3>
  <p>Curabitur vel fermentum augue, quis vulputate diam</p>
</div>

<section class="abs intro">
  <h2>WHAT <em>WE DO ?</em></h2>
  <h4>FACTORY</h4>
  <p>Tolvane security doors combine a high level of security with exceptional value. Our superior quality and proven reliability has made us the first choice for a wide range of companies no matter what their requirement or application. All of our products are designed and manufactured to the highest specification, combine this with a rigorous quality control system</p>
</section>
<div class="abs btn">SEE INDUSTRY</div>

<div class="abs col-rule" style="left:609px"></div>
<div class="abs col-rule" style="left:775px"></div>

<div class="abs service" style="left:608px;top:577px">
  <svg class="hex" width="36" height="40" viewBox="0 0 36 40"><polygon points="18,0 36,10 36,30 18,40 0,30 0,10" fill="#fbd341"/><rect x="11" y="16" width="14" height="5" fill="#2aa7c9"/><rect x="15" y="12" width="6" height="3" fill="#2aa7c9"/><rect x="12" y="22" width="2" height="3" fill="#2aa7c9"/><rect x="22" y="22" width="2" height="3" fill="#2aa7c9"/></svg>
  <h5>INDUSTRIAL PROCESS</h5>
  <p>Curabitur vel fermentum augue, quis vulputate diam</p>
</div>
<div class="abs service" style="left:774px;top:577px">
  <svg class="hex" width="36" height="40" viewBox="0 0 36 40"><polygon points="18,0 36,10 36,30 18,40 0,30 0,10" fill="#fbd341"/><rect x="11" y="16" width="14" height="5" fill="#2aa7c9"/><rect x="15" y="12" width="6" height="3" fill="#2aa7c9"/><rect x="12" y="22" width="2" height="3" fill="#2aa7c9"/><rect x="22" y="22" width="2" height="3" fill="#2aa7c9"/></svg>
  <h5>INDUSTRIAL PROCESS</h5>
  <p>Curabitur vel fermentum augue, quis vulputate diam</p>
</div>
<div class="abs service" style="left:608px;top:679px">
  <svg class="hex" width="36" height="40" viewBox="0 0 36 40"><polygon points="18,0 36,10 36,30 18,40 0,30 0,10" fill="#fbd341"/><rect x="11" y="16" width="14" height="5" fill="#2aa7c9"/><rect x="15" y="12" width="6" height="3" fill="#2aa7c9"/><rect x="12" y="22" width="2" height="3" fill="#2aa7c9"/><rect x="22" y="22" width="2" height="3" fill="#2aa7c9"/></svg>
  <h5>INDUSTRIAL PROCESS</h5>
  <p>Curabitur vel fermentum augue, quis vulputate diam</p>
</div>
<div class="abs service" style="left:774px;top:679px">
  <svg class="hex" width="36" height="40" viewBox="0 0 36 40"><polygon points="18,0 36,10 36,30 18,40 0,30 0,10" fill="#fbd341"/><rect x="11" y="16" width="14" height="5" fill="#2aa7c9"/><rect x="15" y="12" width="6" height="3" fill="#2aa7c9"/><rect x="12" y="22" width="2" height="3" fill="#2aa7c9"/><rect x="22" y="22" width="2" height="3" fill="#2aa7c9"/></svg>
  <h5>INDUSTRIAL PROCESS</h5>
  <p>Curabitur vel fermentum augue, quis vulputate diam</p>
</div>

<div class="abs tech-photo" role="img" aria-label="Machinist setting up a steel part on a CNC drilling machine with blue coolant hoses"></div>
<div class="abs tech-panel"></div>
<section class="abs tech-copy">
  <small>INNOVATION &amp; ADOPTION</small>
  <h2>TECHNOLOGY</h2>
  <p>Lorem ipsum dolor sit amet, consectetur adipisicing elit. Eaque doloremque ipsam optio<br>aliquid et dignissim.</p>
</section>

<div class="abs acc" style="top:938px">
  <div class="acc-head">Colorquibusdam nulla in a est fugiat corporis<span class="acc-toggle"><svg width="9" height="9" viewBox="0 0 9 9"><path d="M1 1h7L1 8h7z" fill="none" stroke="#fff" stroke-width="1.2"/></svg></span></div>
  <div class="acc-body">omnis repellendus consequuntur voluptate quisquam illo natus facilis voluptatum ea ex excepturi facere ipsum assumenda</div>
</div>
<div class="abs acc" style="top:1037px">
  <div class="acc-head">AccordioExplicabo neque eius doloribus<span class="acc-toggle"><svg width="9" height="9" viewBox="0 0 9 9"><circle cx="4.5" cy="4.5" r="2.6" fill="none" stroke="#fff" stroke-width="1.6" stroke-dasharray="1.4 0.8"/></svg></span></div>
</div>
<div class="abs acc" style="top:1070px">
  <div class="acc-head">Colorquibusdam nulla in a est fugiat corporis<span class="acc-toggle"><svg width="9" height="9" viewBox="0 0 9 9"><circle cx="4.5" cy="4.5" r="2.6" fill="none" stroke="#fff" stroke-width="1.6" stroke-dasharray="1.4 0.8"/></svg></span></div>
</div>
<div class="abs acc" style="top:1102px">
  <div class="acc-head">Colorquibusdam nulla in a est fugiat corporis<span class="acc-toggle"><svg width="9" height="9" viewBox="0 0 9 9"><circle cx="4.5" cy="4.5" r="2.6" fill="none" stroke="#fff" stroke-width="1.6" stroke-dasharray="1.4 0.8"/></svg></span></div>
</div>

</body>
</html>
```